Global Weight loss program

we need a business card based in Brooklyn , NY called PeppertonRUN . Mara Dulvik Tenbrook the founder and creator of PeppertonRUN Movement. A business based around nutrition, health, Whole Foods and fitness.

Industry/Entity Type

Food Service

Contact Information for Business Card

Phone number : 718-555-0143
website www.peppertonrun.com
email : mara@peppertonrun.com

Font styles to use
Sans Serif

Requirements
Must have
• logo colors
• green black and gold
Nice to have
• must be simple and sharp.
Should not have
• pictures of items

```html
<!DOCTYPE html>
<html lang="en">
<head>
<meta charset="utf-8">
<title>PeppertonRUN Business Card</title>
<link rel="stylesheet" href="https://fonts.googleapis.com/css2?family=Raleway:wght@400;500;700&display=swap">
<style>
  :root {
    --backdrop: #2b2b2b;
    --card-white: #ffffff;
    --ink: #333333;
    --green-deep: #7dbb42;
    --green-light: #a0cc3a;
    --text-light: #ffffff;
  }
  html, body {
    margin: 0;
    padding: 0;
    width: 1200px;
    height: 930px;
    overflow: hidden;
    background: var(--backdrop);
    font-family: "Raleway", sans-serif;
  }
  .canvas {
    position: relative;
    width: 1200px;
    height: 930px;
  }
  .card {
    position: absolute;
    left: 278px;
    width: 644px;
    height: 368px;
    border-radius: 22px;
    overflow: hidden;
  }
  .card-front {
    top: 76px;
    background: var(--card-white);
  }
  .card-back {
    top: 486px;
    background: linear-gradient(90deg, var(--green-deep), var(--green-light));
  }
  .front-wave {
    position: absolute;
    inset: 0;
  }
  .brand-front {
    position: absolute;
    left: 34px;
    top: 36px;
    width: 232px;
    text-align: center;
  }
  .brand-mark {
    display: block;
    width: 100px;
    height: 100px;
    margin: 0 auto 12px;
    border-radius: 50%;
    background: var(--green-deep);
  }
  .brand-name {
    display: block;
    font-weight: 700;
    font-size: 33px;
    line-height: 1;
    color: var(--ink);
    letter-spacing: -0.5px;
  }
  .brand-tagline {
    display: block;
    margin-top: 4px;
    font-size: 10.5px;
    letter-spacing: 1.6px;
    color: var(--ink);
  }
  .contact {
    position: absolute;
    right: 29px;
    top: 186px;
    text-align: right;
    color: var(--text-light);
    font-size: 16px;
    line-height: 1.25;
  }
  .contact-name {
    font-size: 22px;
    font-weight: 500;
    letter-spacing: 1px;
    margin: 0;
  }
  .contact-role {
    margin: 0 0 9px;
  }
  .contact-address {
    margin: 0 0 9px;
    font-style: normal;
  }
  .contact-lines {
    list-style: none;
    margin: 0;
    padding: 0;
  }
  .contact-lines li {
    display: flex;
    justify-content: flex-end;
    align-items: center;
    gap: 9px;
  }
  .contact-lines svg {
    width: 11px;
    height: 11px;
  }
  .brand-back {
    position: absolute;
    left: 0;
    right: 0;
    top: 80px;
    text-align: center;
    color: var(--text-light);
  }
  .brand-back .brand-mark {
    width: 130px;
    height: 130px;
    margin-bottom: 14px;
    background: var(--text-light);
  }
  .brand-back .brand-name {
    color: var(--text-light);
    font-size: 46px;
  }
  .brand-back .brand-tagline {
    color: var(--text-light);
    font-size: 13px;
    letter-spacing: 2.4px;
    margin-top: 4px;
  }
</style>
</head>
<body>
<main class="canvas">
  <section class="card card-front">
    <svg class="front-wave" viewBox="0 0 644 368" width="644" height="368" aria-hidden="true">
      <defs>
        <linearGradient id="waveGreen" x1="0" y1="0" x2="1" y2="0">
          <stop offset="0" stop-color="#7dbb42"/>
          <stop offset="1" stop-color="#a0cc3a"/>
        </linearGradient>
      </defs>
      <path d="M0,250 C120,300 260,270 400,190 C500,135 590,150 644,180 L644,368 L0,368 Z" fill="url(#waveGreen)"/>
      <path d="M0,268 C130,318 270,292 410,206 C500,152 590,158 644,190" fill="none" stroke="#ffffff" stroke-width="5"/>
      <path d="M40,320 C170,320 300,290 420,216" fill="none" stroke="#ffffff" stroke-width="4"/>
      <path d="M0,255 C110,295 230,285 320,230" fill="none" stroke="#ffffff" stroke-width="3"/>
      <path d="M300,230 C420,160 520,120 620,150" fill="none" stroke="#a0cc3a" stroke-width="6"/>
    </svg>

    <div class="brand-front">
      <span class="brand-mark"></span>
      <span class="brand-name">PeppertonRUN</span>
      <span class="brand-tagline">Fitness, Nutrition and Health</span>
    </div>

    <div class="contact">
      <p class="contact-name">MARA TENBROOK</p>
      <p class="contact-role">Founder</p>
      <address class="contact-address">1480 Wrenfield St.<br>Brooklyn, NY 11201</address>
      <ul class="contact-lines">
        <li>718-555-0143
          <svg viewBox="0 0 12 12" aria-hidden="true"><path d="M3,1 L5,1 L5.5,3.5 L4.2,4.4 C4.8,6 6,7.2 7.6,7.8 L8.5,6.5 L11,7 L11,9 C11,10 10,11 9,11 C5,10.5 1.5,7 1,3 C1,2 2,1 3,1 Z" fill="#ffffff"/></svg>
        </li>
        <li>mara@peppertonrun.com
          <svg viewBox="0 0 12 12" aria-hidden="true"><rect x="1" y="2.5" width="10" height="7" fill="none" stroke="#ffffff" stroke-width="1.2"/><path d="M1,2.5 L6,6.5 L11,2.5" fill="none" stroke="#ffffff" stroke-width="1.2"/></svg>
        </li>
        <li>www.peppertonrun.com
          <svg viewBox="0 0 12 12" aria-hidden="true"><circle cx="6" cy="6" r="5" fill="none" stroke="#ffffff" stroke-width="1"/><ellipse cx="6" cy="6" rx="2.2" ry="5" fill="none" stroke="#ffffff" stroke-width="1"/><path d="M1,6 H11 M2,3.5 H10 M2,8.5 H10" stroke="#ffffff" stroke-width="0.9"/></svg>
        </li>
      </ul>
    </div>
  </section>

  <section class="card card-back">
    <div class="brand-back">
      <span class="brand-mark"></span>
      <span class="brand-name">PeppertonRUN</span>
      <span class="brand-tagline">Fitness, Nutrition and Health</span>
    </div>
  </section>
</main>
</body>
</html>
```